Business Card for Pottery and Jewellery Designer

A new business card design is needed to accompany a newly launching pottery and jewellery website. The company logo has been attached for use. The company is called Glazewick Studio. For a sense of the vibe please see the website (it is currently under construction but this way you'll get a feel for the style) www.GlazewickStudio.com

The website font is Pontano Sans for the body of the text with Overlock for headers.

The overall look should be clean and elegant. The back side can have just the logo. The front side should have a smaller logo and the following details displayed:

Glazewick Studio
Designer: Hollis Marrow
Phone: xxx.xxx.xxxx
Email: Designer@GlazewickStudio.com

The structure of displaying this is completely up to you. Different layouts and creative methods of displaying contact info are welcome as long as it stays clean/uncluttered.

No product photographs are to be included in the design as the catalogue changes quickly.

Colour preferences lean towards elegant and understated (charcoal grey, dark navy blue etc.)

Please let me know if you have any further questions or further details required.

Target Market(s)

Target market is 30+ year old women

Industry/Entity Type

Construction

Colors
ffffff
1b1b1b
474747
d9d9d9
fafafa
0355a3

Requirements
Must have
• The submissions so far have looked very typical and don't stand out right now. They're also all in navy with very little variation. I'm looking for something that stands out a it more while still being clean-looking.
Nice to have
• I've attached a few design samples and an idea for a backdrop. It would be great to see some designs in black, white, and grey with only a hint of color.
Should not have
• Product Images

```html
<!DOCTYPE html>
<html lang="en">
<head>
<meta charset="UTF-8">
<title>Glazewick Studio – Business Card</title>
<link rel="stylesheet" href="https://fonts.googleapis.com/css2?family=Lato:wght@400;700&family=Quicksand:wght@700&display=swap">
<style>
  :root {
    --backdrop: #1b1b1b;
    --card-light: #fafafa;
    --card-dark: #333333;
    --ink: #1b1b1b;
    --ink-soft: #474747;
    --accent: #3d3b9c;
    --accent-soft: #c9c8ee;
    --white: #ffffff;
  }
  * { margin: 0; padding: 0; box-sizing: border-box; }
  html, body {
    width: 1200px;
    height: 800px;
    overflow: hidden;
    background: var(--backdrop);
  }
  .canvas {
    position: relative;
    width: 1200px;
    height: 800px;
    display: flex;
    justify-content: center;
    align-items: center;
    gap: 40px;
  }
  .card {
    position: relative;
    width: 340px;
    height: 595px;
  }
  .card--front { background: var(--card-light); }
  .card--back { background: var(--card-dark); }

  /* Front */
  .brand-small {
    position: absolute;
    top: 40px;
    right: 34px;
    display: flex;
    align-items: center;
    gap: 8px;
    font-family: "Lato", sans-serif;
    font-weight: 700;
    font-size: 15px;
    color: var(--accent);
  }
  .brand-dot {
    width: 14px;
    height: 14px;
    border-radius: 50%;
    background: var(--accent);
  }
  .person {
    position: absolute;
    top: 255px;
    left: 30px;
  }
  .person__name {
    font-family: "Lato", sans-serif;
    font-weight: 400;
    font-size: 27px;
    color: var(--accent);
    line-height: 1.1;
  }
  .person__role {
    font-family: "Quicksand", sans-serif;
    font-weight: 700;
    font-size: 12px;
    color: var(--ink-soft);
    margin-top: 6px;
  }
  .contact {
    position: absolute;
    right: 30px;
    bottom: 85px;
    text-align: right;
    font-family: "Quicksand", sans-serif;
    font-weight: 700;
    color: var(--ink);
    line-height: 1.5;
  }
  .contact__phone { font-size: 17px; letter-spacing: 2px; }
  .contact__email,
  .contact__web { font-size: 13.5px; }

  /* Back */
  .brand-large {
    position: absolute;
    top: 200px;
    left: 0;
    right: 0;
    display: flex;
    flex-direction: column;
    align-items: center;
    text-align: center;
  }
  .brand-large__mark {
    width: 110px;
    height: 110px;
    border-radius: 50%;
    background: var(--white);
    margin-bottom: 26px;
  }
  .brand-large__name {
    font-family: "Lato", sans-serif;
    font-weight: 400;
    font-size: 27px;
    color: var(--accent-soft);
  }
  .brand-large__web {
    font-family: "Quicksand", sans-serif;
    font-weight: 700;
    font-size: 12px;
    color: var(--white);
    margin-top: 6px;
    letter-spacing: 0.5px;
  }
</style>
</head>
<body>
  <main class="canvas">
    <section class="card card--front" aria-label="Card front">
      <div class="brand-small">
        <span class="brand-dot"></span>
        <span>Glazewick Studio</span>
      </div>
      <div class="person">
        <p class="person__name">Hollis Marrow</p>
        <p class="person__role">Designer</p>
      </div>
      <div class="contact">
        <p class="contact__phone">xxx.xxx.xxxx</p>
        <p class="contact__email">Designer@GlazewickStudio.com</p>
        <p class="contact__web">www.GlazewickStudio.com</p>
      </div>
    </section>

    <section class="card card--back" aria-label="Card back">
      <div class="brand-large">
        <span class="brand-large__mark"></span>
        <p class="brand-large__name">Glazewick Studio</p>
        <p class="brand-large__web">www.GlazewickStudio.com</p>
      </div>
    </section>
  </main>
</body>
</html>
```